To design a look and feel for a website. The company offers technical services to governemtns and public bodies. It does NOT market to the public.

The core business is GIS (Geographic Information Systems)

The site needs to be clean and simple, The current version is available here: www.velda.ie

Target Market(s)

Goverment agencies and public bodies in the EU, buying through the public procurerment process

Requirements
Should not have
• corny graphics of hands holding globes or sateliites please.

```html
<!DOCTYPE html>
<html lang="en">
<head>
<meta charset="utf-8">
<title>The VELDA Group – Information Expertise</title>
<link rel="stylesheet" href="https://fonts.googleapis.com/css2?family=Open+Sans:wght@400;600&family=Arimo:wght@400;700&display=swap">
<style>
  :root {
    --brand-blue: #1d3d8f;
    --brand-violet: #6a62b8;
    --text-grey: #666;
    --text-dark: #333;
    --line-grey: #c8c8c8;
    --hero-dark: #3a3a3a;
    --hero-light: #e8e8e8;
    --white: #fff;
  }
  * { box-sizing: border-box; margin: 0; padding: 0; }
  html, body { width: 1200px; height: 909px; overflow: hidden; background: var(--white); }
  body { font-family: "Arimo", Arial, sans-serif; color: var(--text-grey); position: relative; }
  .page { position: absolute; left: 180px; top: 0; width: 840px; }

  .site-header { height: 100px; position: relative; }
  .brand { position: absolute; left: 2px; top: 18px; color: var(--brand-blue); }
  .brand-the { font-size: 9px; font-weight: 700; }
  .brand-name { font-family: "Open Sans", sans-serif; font-size: 30px; letter-spacing: 1px; line-height: 30px; }
  .brand-sub { font-size: 8px; color: var(--brand-violet); }
  .main-nav { position: absolute; right: 8px; top: 52px; display: flex; gap: 56px; font-size: 13px; color: var(--text-dark); }

  .hero { position: absolute; top: 100px; left: 0; width: 840px; height: 254px;
    background: linear-gradient(100deg, var(--hero-dark) 0%, #555 45%, var(--hero-light) 78%, #9a9a9a 100%); }
  .hero-shadow { position: absolute; top: 354px; left: 6px; width: 828px; height: 18px;
    background: radial-gradient(ellipse at top, rgba(0,0,0,.35), rgba(0,0,0,0) 70%); }
  .hero-copy { position: absolute; left: 52px; top: 84px; color: var(--white); }
  .hero-kicker { font-family: "Open Sans", sans-serif; font-size: 18px; }
  .hero-title { font-family: "Open Sans", sans-serif; font-size: 24px; margin-top: 2px; }
  .hero-text { font-size: 12.5px; line-height: 20.5px; margin-top: 10px; width: 380px; }
  .hero-figure { position: absolute; right: 110px; top: 8px; width: 90px; height: 240px;
    background: linear-gradient(#4a4a4a, #222); border-radius: 40px 40px 6px 6px; opacity: .55; }
  .slider-dots { position: absolute; right: 10px; bottom: 10px; display: flex; gap: 2px; }
  .slider-dots span { width: 7px; height: 7px; background: var(--white); }
  .slider-dots span.active { background: var(--brand-blue); }

  .services { position: absolute; top: 395px; left: 0; width: 840px; display: flex; justify-content: space-between; }
  .service { width: 190px; }
  .service h2 { font-weight: 400; font-size: 14px; color: var(--brand-blue); height: 29px; }
  .service-photo { width: 190px; height: 116px; }
  .service p { font-size: 10.5px; line-height: 20px; margin-top: 9px; }

  .welcome { position: absolute; top: 616px; left: 0; width: 840px; }
  .welcome h2 { font-weight: 400; font-size: 14.5px; color: var(--brand-blue); }
  .welcome p { font-size: 11.5px; line-height: 20.5px; margin-top: 12px; }

  .clients { position: absolute; top: 731px; left: 0; width: 840px; height: 76px; border: 1px solid var(--line-grey);
    display: flex; align-items: center; justify-content: space-around; padding: 0 10px; }
  .client { display: flex; align-items: center; gap: 5px; font-size: 12px; font-weight: 700; color: var(--brand-blue); }
  .client i { display: block; width: 12px; height: 12px; border-radius: 50%; background: var(--brand-blue); }
  .client-badge { width: 50px; height: 50px; border-radius: 50%; background: #a9bfe0; }

  .site-footer { position: absolute; top: 821px; left: 0; width: 840px; height: 62px;
    background: linear-gradient(#ebebeb, var(--white) 55%); }
  .footer-nav { position: absolute; left: 20px; top: 20px; font-size: 9.5px; color: var(--text-dark); }
  .footer-nav span { margin: 0 13px; }
  .copyright { position: absolute; left: 20px; top: 44px; font-size: 9.5px; color: var(--text-dark); }
  .social { position: absolute; right: 18px; top: 20px; display: flex; gap: 3px; }
  .social span { width: 26px; height: 26px; border-radius: 50%; color: var(--white); font-size: 7px;
    display: flex; align-items: center; justify-content: center; }
</style>
</head>
<body>
<div class="page">
  <header class="site-header">
    <div class="brand">
      <div class="brand-the">THE</div>
      <div class="brand-name">VELDA</div>
      <div class="brand-sub">information Expertise</div>
    </div>
    <nav class="main-nav"><span>Home</span><span>Services</span><span>Clients</span><span>Contact</span><span>Inspire</span></nav>
  </header>

  <section class="hero">
    <div class="hero-figure" role="img" aria-label="Businessman pulling a rope across a grid floor"></div>
    <div class="hero-copy">
      <div class="hero-kicker">THE VELDA GROUP</div>
      <div class="hero-title">INFORMATION EXPERTISE</div>
      <p class="hero-text">The VELDA Group has been in business since 1994 and continues to develop and update its range of services.</p>
    </div>
    <div class="slider-dots"><span class="active"></span><span></span><span></span><span></span><span></span></div>
  </section>
  <div class="hero-shadow"></div>

  <section class="services">
    <article class="service">
      <h2>Data Management</h2>
      <div class="service-photo" role="img" aria-label="Woman using a holographic data interface" style="background:linear-gradient(120deg,#1a7fb8,#7fd0ef 55%,#2a8cc4)"></div>
      <p>VELDA has extensive experience in Spatial Data processing. Services include:</p>
    </article>
    <article class="service">
      <h2>Spatial Data</h2>
      <div class="service-photo" role="img" aria-label="Businessman standing beside a large globe" style="background:linear-gradient(90deg,#8a9096,#e9ecee 60%,#fafafa)"></div>
      <p>VELDA has extensive experience in Spatial Data processing. Services include:</p>
    </article>
    <article class="service">
      <h2>Land Use</h2>
      <div class="service-photo" role="img" aria-label="Lone tree in a green field under a cloudy sky" style="background:linear-gradient(#5d9bd6,#d8e8f4 60%,#5e8f2c 78%,#3d6e1c)"></div>
      <p>VELDA has extensive experience in Spatial Data processing. Services include:</p>
    </article>
    <article class="service">
      <h2>Transport</h2>
      <div class="service-photo" role="img" aria-label="Businessman on a wooden pier above the clouds" style="background:linear-gradient(#a9cbe6,#e4eef6 55%,#b6c8d6)"></div>
      <p>VELDA has extensive experience in Spatial Data processing. Services include:</p>
    </article>
  </section>

  <section class="welcome">
    <h2>Welcome to The VELDA Group</h2>
    <p>The VELDA Group has been in business since 1994 and continues to develop and update its range of services. The company has a high level of expertise in handling data and information, and in building and re-engineering database systems. We have a particular expertise in working with Irish data sets and have a strong grounding in dealing with spatial data.</p>
  </section>

  <section class="clients" aria-label="Clients">
    <div class="client"><i></i>Norvale</div>
    <div class="client">Brindmoor</div>
    <div class="client-badge" aria-label="Unisfield" role="img"></div>
    <div class="client">Arbora</div>
    <div class="client">Statwell</div>
    <div class="client">Harlow PM</div>
    <div class="client">Kestra</div>
    <div class="client">Coastline Bus</div>
  </section>

  <footer class="site-footer">
    <div class="footer-nav">Home<span>|</span>Services<span>|</span>Clients<span>|</span>Contact<span>|</span>Inspire</div>
    <div class="copyright">Copyright: The VELDA group Ltd 2013. All rights reserved.</div>
    <div class="social">
      <span style="background:#2f5fb3">Cirk</span>
      <span style="background:#3fa9e0">Chirp</span>
      <span style="background:#1d7fa8">Lnk</span>
      <span style="background:#f0a21e">Feed</span>
    </div>
  </footer>
</div>
</body>
</html>
```